Duel Business card

Want an edgy business card that shows both of our companies on each side of the card, OR both together with a cool design.

*Must be edgy: We have attached our two business logos. We are a bail bond and immigration bond company.

Would like the address on one side only.
Need Phone, cell, website, address, and Name

Company Name 1: Liberty Release Partners
www.libertyreleasepartners-example.com

Company Name 2: Crossway Custody Advocates
www.crosswaycustodyadvocates-example.com

These cards will need to be easily changeable so I can modify new employees

Target Market(s)

people in jail, takign imigrants out of jail and from being taken back to there country

Industry/Entity Type

Business

Requirements
Must have
• Include both logos attached

```html
<!DOCTYPE html>
<html lang="en">
<head>
<meta charset="utf-8">
<title>Dual Business Card – Crossway Custody Advocates / Liberty Release Partners</title>
<link rel="stylesheet" href="https://fonts.googleapis.com/css2?family=Oswald:wght@400;500;600;700&display=swap">
<style>
  :root {
    --page-bg: #e4e5e7;
    --card-dark: #0c0c0d;
    --white: #ffffff;
    --red: #e0322b;
    --crossway-blue: #2f78d0;
    --liberty-blue: #3b63d4;
    --liberty-gold: #f0b51c;
  }
  * { margin: 0; padding: 0; box-sizing: border-box; }
  html, body {
    width: 1068px;
    height: 1200px;
    overflow: hidden;
    background: var(--page-bg);
    font-family: "Oswald", "Arial Narrow", sans-serif;
  }
  .sheet { position: relative; width: 1068px; height: 1200px; }
  .card {
    position: absolute;
    left: 94px;
    width: 880px;
    height: 503px;
    overflow: hidden;
    background: var(--card-dark);
    box-shadow: 0 10px 28px rgba(0,0,0,0.25);
  }
  .card--crossway { top: 64px; }
  .card--liberty { top: 633px; }

  .card__art { position: absolute; inset: 0; width: 880px; height: 503px; }
  .card__emblem {
    position: absolute;
    border-radius: 50%;
    background: radial-gradient(closest-side, rgba(120,120,125,0.22), rgba(60,60,64,0.08) 70%, rgba(0,0,0,0));
  }
  .card--crossway .card__emblem { left: 360px; top: 40px; width: 360px; height: 300px; }
  .card--liberty .card__emblem { left: 330px; top: 110px; width: 340px; height: 320px; }

  .rotated {
    position: absolute;
    transform-origin: 0 0;
    white-space: nowrap;
  }
  .rotated--fall { transform: rotate(50deg); }
  .rotated--rise { transform: rotate(-27deg); }

  .identity .person-name {
    font-size: 56px;
    font-weight: 700;
    line-height: 1;
    letter-spacing: 0.2px;
    color: var(--white);
  }
  .identity .person-title {
    padding-left: 30px;
    margin-top: 4px;
    font-size: 22px;
    font-weight: 500;
    line-height: 1;
    color: var(--white);
  }
  .card--crossway .surname { color: var(--crossway-blue); }
  .card--liberty .surname { color: var(--liberty-gold); }

  .contacts div {
    font-size: 15px;
    font-weight: 500;
    line-height: 28px;
    color: var(--white);
  }
  .contacts .contact-line--gap { margin-top: 28px; }
  .card--crossway .contact-line--web { color: var(--crossway-blue); }
  .card--liberty .contact-line--web { color: var(--liberty-gold); }

  .company { display: flex; align-items: center; gap: 10px; height: 28px; }
  .company__dot { width: 28px; height: 28px; border-radius: 50%; flex: none; }
  .card--crossway .company__dot { background: var(--crossway-blue); }
  .card--liberty .company__dot { background: var(--liberty-gold); }
  .company__name {
    font-size: 19px;
    font-weight: 600;
    line-height: 28px;
    color: var(--white);
  }
</style>
</head>
<body>
<main class="sheet">

  <section class="card card--crossway">
    <svg class="card__art" viewBox="0 0 880 503" aria-hidden="true">
      <defs>
        <linearGradient id="crossway-bg" x1="0" y1="0" x2="1" y2="1">
          <stop offset="0" stop-color="#1a1b1d"/>
          <stop offset="1" stop-color="#09090a"/>
        </linearGradient>
        <linearGradient id="red-sheen-a" x1="0" y1="1" x2="1" y2="0">
          <stop offset="0" stop-color="#e0322b"/>
          <stop offset="0.75" stop-color="#e0322b"/>
          <stop offset="0.88" stop-color="#ffffff"/>
          <stop offset="1" stop-color="#e0322b"/>
        </linearGradient>
        <linearGradient id="red-sheen-b" x1="0" y1="0" x2="1" y2="1">
          <stop offset="0" stop-color="#e0322b"/>
          <stop offset="0.12" stop-color="#ffffff"/>
          <stop offset="0.3" stop-color="#e0322b"/>
          <stop offset="1" stop-color="#e0322b"/>
        </linearGradient>
      </defs>
      <rect width="880" height="503" fill="url(#crossway-bg)" role="img" aria-label="dark hexagonal mesh texture"/>
      <polygon points="330,0 640,0 880,286 880,503 752,503" fill="#2a2b2e" opacity="0.85"/>
      <polygon points="330,0 372,0 794,503 752,503" fill="#131315" opacity="0.9"/>
      <line x1="0" y1="300" x2="357" y2="0" stroke="url(#red-sheen-a)" stroke-width="9"/>
      <line x1="693" y1="0" x2="880" y2="263" stroke="url(#red-sheen-b)" stroke-width="9"/>
      <line x1="440" y1="420" x2="484" y2="503" stroke="var(--red)" stroke-width="9"/>
    </svg>
    <div class="card__emblem" role="img" aria-label="faint large company emblem decoration"></div>

    <div class="rotated rotated--fall identity" style="left:383px; top:14px;">
      <div class="person-name">Firstname <span class="surname">Surname</span></div>
      <div class="person-title">position</div>
    </div>

    <div class="rotated rotated--rise contacts" style="left:22px; top:334px;">
      <div class="contact-line">1234, Adress Lane Adress City, EX 12345</div>
      <div class="contact-line">Phone: 877-555-0142&nbsp;&nbsp;Cell phone: 123-456-789</div>
      <div class="contact-line contact-line--web contact-line--gap">info@crosswaycustodyadvocates-example.com</div>
      <div class="contact-line contact-line--web">www.crosswaycustodyadvocates-example.com</div>
    </div>

    <div class="rotated rotated--rise company" style="left:292px; top:428px;">
      <span class="company__dot"></span>
      <span class="company__name">Crossway Custody Advocates</span>
    </div>
  </section>

  <section class="card card--liberty">
    <svg class="card__art" viewBox="0 0 880 503" aria-hidden="true">
      <defs>
        <linearGradient id="liberty-bg" x1="0" y1="0" x2="1" y2="1">
          <stop offset="0" stop-color="#1a1b1d"/>
          <stop offset="1" stop-color="#09090a"/>
        </linearGradient>
        <linearGradient id="blue-sheen-a" x1="0" y1="1" x2="1" y2="0">
          <stop offset="0" stop-color="#3b63d4"/>
          <stop offset="0.72" stop-color="#3b63d4"/>
          <stop offset="0.86" stop-color="#f0b51c"/>
          <stop offset="1" stop-color="#3b63d4"/>
        </linearGradient>
        <linearGradient id="blue-sheen-b" x1="0" y1="0" x2="1" y2="1">
          <stop offset="0" stop-color="#3b63d4"/>
          <stop offset="0.3" stop-color="#3b63d4"/>
          <stop offset="0.42" stop-color="#f0b51c"/>
          <stop offset="0.55" stop-color="#3b63d4"/>
          <stop offset="1" stop-color="#3b63d4"/>
        </linearGradient>
      </defs>
      <rect width="880" height="503" fill="url(#liberty-bg)" role="img" aria-label="dark hexagonal mesh texture"/>
      <polygon points="290,0 610,0 880,322 880,503 712,503 300,12" fill="#2a2b2e" opacity="0.85"/>
      <polygon points="290,0 332,0 754,503 712,503" fill="#131315" opacity="0.9"/>
      <line x1="0" y1="275" x2="328" y2="0" stroke="url(#blue-sheen-a)" stroke-width="9"/>
      <line x1="80" y1="0" x2="200" y2="135" stroke="var(--liberty-blue)" stroke-width="9"/>
      <line x1="680" y1="0" x2="880" y2="300" stroke="url(#blue-sheen-b)" stroke-width="9"/>
      <line x1="425" y1="415" x2="470" y2="503" stroke="var(--liberty-blue)" stroke-width="9"/>
    </svg>
    <div class="card__emblem" role="img" aria-label="faint large company emblem decoration"></div>

    <div class="rotated rotated--fall identity" style="left:390px; top:14px;">
      <div class="person-name">Firstname <span class="surname">Surname</span></div>
      <div class="person-title">position</div>
    </div>

    <div class="rotated rotated--rise contacts" style="left:12px; top:344px;">
      <div class="contact-line">Phone: 1-888-555-0176&nbsp;&nbsp;Cell phone: 123-456-789</div>
      <div class="contact-line contact-line--web contact-line--gap">info@libertyreleasepartners-example.com</div>
      <div class="contact-line contact-line--web">www.libertyreleasepartners-example.com</div>
    </div>

    <div class="rotated rotated--rise company" style="left:270px; top:432px;">
      <span class="company__dot"></span>
      <span class="company__name">Liberty Release Partners</span>
    </div>
  </section>

</main>
</body>
</html>
```